physio rehab flyer for Vela Motion please

Specification:
Flyer is to be trifold from letter size (8.5 x 11)
-----------------------This may help you:--------------------------
I would like the look of :
clean, minimalistic look with mainly blue and green
san serif font
professional
The colors I like are blue (not the blue in the logo enclosed, I want a change, but more like the blue on my website logo) and light green.
This is my website: www.velamotiongroup.ca just so you get an idea but it will be totally changed soon to a to be determined design.
I like the blue and green in file "sample 2" (enclosed)
I like the pictures in "sample 2" file enclosed
For inspiration, I like design of this brochure: http://www.qlx.ca/HarbourRestore/PatientsFamilies/Clinics_Tests/DAWL_Service/Documents/Brochure.pdf
Here's how I see the pages layout:
----[location: this should be the cover (outside, right panel of trifold)]-----
Vela Motion Logo
Integrated Injury Rehab
Evidence-based, one-on-one care to make your recovery fast and comfortable
www.velamotiongroup.ca
---------------[location: inside, left panel]----------------------------------------
Our team leaders
[portrait here]
Harriet Osei, MD, FRCPC, MSC, CIME
Physiatrist
Dr. Osei specializes in injury rehab and sports medicine. She is highly trained having received her MD and Residency in Physiatry from Wexmoor University. Her passion is to help injured people get back to their life.
[portrait here]
Dorothy Varga, PT
Physiotherapist
Dorothy has over 10 years of experience as a Physiotherapist (5 in Canada). She has advanced training in orthopedics and manual therapy. She loves and relates well with people from the youngest to the most senior.
--------------------[location: inside, middle panel]-------------------------------
Our services
We provide integrated assessment and care from interprofessional team of regulated healthcare professionals with proven experience in injury rehabilitation:
physiatrists
sport medicine physicians
physiotherapists
chiropractors
massage therapists
acupuncturists
psychologists
We provide custom medical bracing, orthotics, orthopedic shoes, assistive devices, and medical stockings, all in one place.
----------------------[location: inside, right panel]-----------------------------------
Only registered physiotherapists
We strongly believe in consistency with your treatment plan. This means that you spend your time here one-on-one with your physiotherapist, not any students or assistants. You get consistent high quality care from a professional.
One-on-one attention
We book maximum 3 people per hour to ensure everyone gets adequate one-on-one time with their physiotherapist. This compares favorably with other clinics, who may book upwards of 5-6 per hour. The atmosphere is professional -balanced with friendly, caring and relaxed. Our highly qualified staff operate this way to help make your recovery faster and more enjoyable.
------------------------[location: outside, left panel]---------------------------------
The right rehab for your clients
Timely access to comprehensive assessment and treatment
Proven track record in injury rehabilitation
Convenient one-stop service
Customized treatment plans
Integrated, co-ordinated care
Evidence-based care applying leading best practices
Access to specialty clinics: Physiatry and Chronic Pain
-------------------------[location: outside, middle panel]--------------------------
Please call us 416-738-4062
for more information on injury rehabilitation
Vela Motion Group
8120 Tolliver Rd., Unit 9
Scarborough, ON M4K 8B2
[Please include a line art map designed based on "map" file enclosed]
To make a referral for your clients, contact velamotiongroup@brisklane.ca or fax: 416-738-4059. Thank you.
www.velamotiongroup.ca
------------------------------------------------------------------------------------------------
Target Market(s)
family doctors, ER docs, lawyers, and general public age (20-50)
Industry/Entity Type
Health And Wellness
Requirements
Must have
- san serif font
- blue and green colors
- clean, sophisticated look
Nice to have
- consumer choice award badge either on front or back of trifold
Should not have
- see above

```html
<!DOCTYPE html>
<html lang="en">
<head>
<meta charset="utf-8">
<title>Vela Motion Group – Our Services</title>
<link href="https://fonts.googleapis.com/css2?family=Didact+Gothic&family=Montserrat:wght@600;700&display=swap" rel="stylesheet">
<style>
  :root{
    --brand-blue:#1c6fc1;
    --ink:#1e1e1e;
    --paper:#ffffff;
    --label-bg:rgba(255,255,255,0.82);
    --photo-warm-a:#c9a27c;
    --photo-warm-b:#e9e2d8;
    --photo-cool-a:#dfe6e8;
    --photo-cool-b:#b8c6cc;
    --photo-clinic-a:#e6eef5;
    --photo-clinic-b:#9fb6c9;
  }
  *{box-sizing:border-box;margin:0;padding:0}
  html,body{width:1200px;height:928px;overflow:hidden;background:var(--paper)}
  .panel-sheet{position:relative;width:1200px;height:928px;background:var(--paper);color:var(--ink);
    font-family:"Didact Gothic",sans-serif}

  .band{position:absolute;background:var(--brand-blue)}
  .band--top-thick{left:384px;right:0;top:78px;height:12px}
  .band--top-thin{left:384px;right:0;top:98px;height:5px}
  .band--bottom-thick{left:0;right:0;top:898px;height:12px}
  .band--bottom-thin{left:0;right:0;top:918px;height:6px}

  .portrait{position:absolute;border:6px solid var(--brand-blue);overflow:hidden;background:var(--paper)}
  .portrait__image{position:absolute;inset:0}
  .portrait--lead{left:50px;top:36px;width:332px;height:334px}
  .portrait--lead .portrait__image{background:linear-gradient(160deg,var(--photo-warm-a),var(--photo-warm-b) 70%)}
  .portrait--physio{left:50px;top:540px;width:334px;height:222px}
  .portrait--physio .portrait__image{background:linear-gradient(90deg,var(--photo-cool-b),var(--photo-cool-a) 45%,var(--photo-cool-b))}
  .portrait__label{position:absolute;left:0;right:0;bottom:0;background:var(--label-bg);text-align:center;padding:4px 0 4px}
  .portrait__name{font-family:"Montserrat",sans-serif;font-weight:700;font-size:20px;letter-spacing:.5px;line-height:24px}
  .portrait__role{font-size:14.5px;letter-spacing:.6px;line-height:18px}

  .bio{position:absolute;left:14px;width:374px;font-size:17px;line-height:23.5px;letter-spacing:.15px}
  .bio--lead{top:382px}
  .bio--physio{top:770px}

  .services{position:absolute;left:440px;width:480px;text-align:center}
  .services__title{position:absolute;left:440px;top:112px;width:480px;text-align:center;
    font-family:"Montserrat",sans-serif;font-weight:700;font-size:46px;letter-spacing:3px;color:var(--brand-blue)}
  .services__intro{position:absolute;left:462px;top:178px;width:440px;font-size:21.5px;line-height:28.5px;text-align:left}
  .services__list{position:absolute;left:456px;top:314px;width:444px;height:238px;border:5px solid var(--brand-blue);
    list-style:none;display:flex;flex-direction:column;justify-content:center;text-align:center}
  .services__list li{font-family:"Montserrat",sans-serif;font-weight:600;font-size:22.5px;letter-spacing:1.4px;line-height:30px;text-transform:uppercase}
  .services__products{position:absolute;left:450px;top:572px;width:460px;font-size:22px;line-height:28px;text-align:center}
  .services__photo{position:absolute;left:516px;top:672px;width:312px;height:204px;border:5px solid var(--brand-blue);
    background:linear-gradient(120deg,var(--photo-clinic-a),var(--photo-clinic-b))}

  .promise{position:absolute;left:930px;width:258px}
  .promise__title{font-family:"Montserrat",sans-serif;font-weight:700;font-size:20.5px;line-height:23px;text-align:center;letter-spacing:.6px}
  .promise__text{font-size:18px;line-height:22.8px;text-align:justify;margin-top:8px;letter-spacing:.4px}
  .promise--registered{top:144px}
  .promise--attention{top:466px}
</style>
</head>
<body>
<main class="panel-sheet">
  <div class="band band--top-thick"></div>
  <div class="band band--top-thin"></div>

  <figure class="portrait portrait--lead">
    <div class="portrait__image" role="img" aria-label="Portrait of Dr. Harriet Osei in a white coat with a stethoscope, in front of file shelves"></div>
    <figcaption class="portrait__label">
      <div class="portrait__name">Harriet Osei</div>
      <div class="portrait__role">MD, FRCPC, MSC, CIME, Physiatrist</div>
    </figcaption>
  </figure>
  <p class="bio bio--lead">Dr. Osei specializes in injury rehab and sports medicine. She is highly trained having received her MD and Residency in Physiatry from Wexmoor University. Her passion is to help injured people het back to their life.</p>

  <figure class="portrait portrait--physio">
    <div class="portrait__image" role="img" aria-label="Portrait of physiotherapist Dorothy Varga in a clinic hallway"></div>
    <figcaption class="portrait__label">
      <div class="portrait__name">Dorothy Varga</div>
      <div class="portrait__role">PT, Physiotherapist</div>
    </figcaption>
  </figure>
  <p class="bio bio--physio">Dorothy has over 10 years of experience as a Physoptherapist (5 in Canada). She has advanced training in orthopedics and manial therapy. She loves and relates well with people form the youngest to the most senior.</p>

  <h1 class="services__title">OUR SERVICES</h1>
  <p class="services__intro">We provide integrated assessment and care from interprofessional team of regulated healthcare profrectionals with proven experience in injury rehabilitation:</p>
  <ul class="services__list">
    <li>Physiatrsists</li>
    <li>Sports Medicine Physicians</li>
    <li>Physiotherapists</li>
    <li>Chiropractors</li>
    <li>Massage Therapists</li>
    <li>Acupuncturists</li>
    <li>Psychologists</li>
  </ul>
  <p class="services__products">We provide custom medical bracing, orthotics, orthopedic shoes, assistive devices and medical stockings, all in one place.</p>
  <div class="services__photo" role="img" aria-label="Therapist fitting a knee brace on a patient's leg"></div>

  <section class="promise promise--registered">
    <h2 class="promise__title">ONLY REGISTERED PHYSIOTHERAPISTS</h2>
    <p class="promise__text">We strongly believe in consistency with your treatment plan. This means that you spend your time here one-on-one with your physiotherapist, not any students or assistants. You get consistent high quality care from a professional.</p>
  </section>

  <section class="promise promise--attention">
    <h2 class="promise__title">ONE-ON-ONE ATTENTION</h2>
    <p class="promise__text">We book maximum 3 people per hour to ensure everyone gets adequate one-on-one time with their physiotherapist. This compares favorably with other clients, who may book upwards of 5-6 per hour. The atmosphere is professional - balanced with friendly, caring and relaxed. Our highly qualified staff operate this way to help make your recovery faster and more enjoyable.</p>
  </section>

  <div class="band band--bottom-thick"></div>
  <div class="band band--bottom-thin"></div>
</main>
</body>
</html>
```